Flyer Design Project

Our company focuses on selling Consumer products like home furniture, home decor, electronics and accessories by public auction. We need a flyer design that will showcase these products with pictures and text. Illustration and desciption on the flyer is always genetic and never changes, The flyer design should be simple and straight forward with limited graphic design and instead focus on product description and emphasise on words Public Auction, and the word AUCTION being the main heading on the flyer. Multilpe colours are prefered.

Target Market(s)

Age group between 30-65 lmajority living in rural, homeowners and looking for a great quality product at an economical price

Industry/Entity Type

Graphic Design

Requirements
Must have
• The flyer should be tri-fold 11x17 inches in size fron and back.
Nice to have
• To show consumers that they have an opportunity to save money by attending our auctions.
Should not have
• The flyer design should not look too corporate or sophisticated. Simple approach to target consumers since most of them live in rural areas.

```html
<!DOCTYPE html>
<html lang="en">
<head>
<meta charset="utf-8">
<title>Public Auction Tri-fold Flyer</title>
<link href="https://fonts.googleapis.com/css2?family=Passion+One:wght@700&family=Fredoka:wght@500;600&family=Delius+Unicase:wght@400;700&display=swap" rel="stylesheet">
<style>
  :root {
    --bg: #ece8e2;
    --pink: #ef3b63;
    --pink-deep: #e8355f;
    --orange: #f47a45;
    --amber: #f6a03a;
    --yellow: #f5c42c;
    --ink: #1d1a17;
    --tag: rgba(244, 128, 70, 0.85);
    --tag-warm: rgba(246, 170, 60, 0.9);
    --cream: #fff6df;
  }
  * { box-sizing: border-box; margin: 0; padding: 0; }
  html, body { width: 1200px; height: 947px; overflow: hidden; }
  body {
    background: var(--bg);
    position: relative;
    font-family: "Delius Unicase", "Comic Sans MS", sans-serif;
    color: var(--ink);
  }

  /* Inside spread */
  .spread {
    position: absolute; left: 40px; top: 150px;
    width: 750px; height: 620px;
    display: flex;
    box-shadow: 0 14px 30px rgba(0,0,0,.25);
  }
  .panel { width: 250px; height: 100%; position: relative; }
  .panel--inventory { background: linear-gradient(160deg, var(--pink) 0%, #f04c5e 100%); }
  .panel--list-a { background: linear-gradient(160deg, #f06a55 0%, var(--amber) 100%); }
  .panel--list-b { background: linear-gradient(160deg, var(--amber) 0%, var(--yellow) 100%); }
  .panel + .panel { border-left: 1px solid rgba(0,0,0,.08); }

  .authorized {
    position: absolute; left: 0; top: 20px; width: 250px;
    background: var(--yellow);
    padding: 8px 12px;
    text-align: center;
    font-size: 11px; line-height: 1.3;
  }
  .authorized__name { display: block; font-size: 17px; font-weight: 700; }
  .product-gallery {
    position: absolute; left: 18px; top: 95px;
    width: 214px; height: 500px;
    border-radius: 4px;
    background: linear-gradient(180deg, rgba(120,70,50,.35), rgba(60,40,40,.3));
  }

  .tag-list {
    list-style: none;
    position: absolute; left: 16px; right: 16px; top: 30px; bottom: 20px;
    display: flex; flex-direction: column; justify-content: space-between;
  }
  .tag {
    background: var(--tag);
    padding: 8px 10px;
    font-size: 10.5px; line-height: 1.35;
    text-align: center; text-transform: uppercase;
    box-shadow: 2px 3px 5px rgba(0,0,0,.25);
  }
  .panel--list-a .tag { background: var(--tag-warm); }

  /* Front cover */
  .cover {
    position: absolute; left: 840px; top: 150px;
    width: 320px; height: 620px;
    background: linear-gradient(180deg, var(--amber) 0%, var(--yellow) 60%);
    box-shadow: 0 14px 30px rgba(0,0,0,.25);
    overflow: hidden;
    text-align: center;
  }
  .cover__lead {
    margin: 48px 18px 0;
    font-family: "Fredoka", sans-serif; font-weight: 600;
    font-size: 19px; line-height: 1.15; text-transform: uppercase;
  }
  .cover__title {
    margin-top: 18px;
    font-family: "Passion One", Impact, sans-serif;
    font-size: 86px; line-height: .9;
    color: var(--pink);
    text-shadow: 3px 3px 0 var(--ink);
    letter-spacing: 1px;
  }
  .cover__badge {
    position: relative; width: 180px; height: 86px;
    margin: 26px auto 0;
  }
  .cover__badge svg { position: absolute; inset: 0; }
  .cover__badge p {
    position: relative; padding-top: 18px;
    font-family: "Fredoka", sans-serif; font-weight: 500;
    color: #fff; font-size: 15px; line-height: 1.2;
  }
  .cover__band { position: absolute; left: 0; bottom: 0; width: 100%; height: 110px; }
  .cover__furniture {
    position: absolute; left: 24px; right: 24px; bottom: 40px; height: 125px;
    background: linear-gradient(180deg, rgba(29,26,23,.75), rgba(29,26,23,.9));
    border-radius: 6px;
  }
</style>
</head>
<body>
  <section class="spread">
    <div class="panel panel--inventory">
      <p class="authorized"><span class="authorized__name">Dale Whitfield.</span>Auctioneer has been authorized to liquidate the following INVENTORY</p>
      <div class="product-gallery" role="img" aria-label="Collage of cut-out product photos: furniture, clocks, cookware, electronics, rugs, mattresses and décor"></div>
    </div>
    <div class="panel panel--list-a">
      <ul class="tag-list">
        <li class="tag">18/10 stainless steel cookware sets, knife sets with block, cutlery sets with display cases.</li>
        <li class="tag">Selection of name brand LCD and plasma HDTVs, DVD, Blu-ray players, home theatre surround sound systems.</li>
        <li class="tag">High quality (made in Canada) orthopedic pillow top mattress sets in queen and king size.</li>
        <li class="tag">Stunnding dining room suites, also to include pub and dinette sets in mahogany, walnut, oak and cherry.</li>
        <li class="tag">Large wall clocks, 31-day grandfather clocks, various decorative signs, display cases, china and curio cabinets, modelships.</li>
        <li class="tag">Bedroom suites to include mission, plataform, sleigh, and poster beds in queen anne, victorian louis phillip, and french accented designs in queen and king sizes.</li>
      </ul>
    </div>
    <div class="panel panel--list-b">
      <ul class="tag-list">
        <li class="tag">Occasional tables, corner tables, sofa tables, coffee and end table sets.</li>
        <li class="tag">Home decor items including lamps, wall mirrors, TV stands, storage ottomans, diverse selection of collector's artwork for investment by known &amp; respected Canadian artists.</li>
        <li class="tag">Replica guns w/shadowbox display cases, diecast model cars, various collectible figures</li>
        <li class="tag">Earrings &amp; necklacs, nostalgia items, decorative and display swords, large, medium and small size decorative vases</li>
        <li class="tag">High quality imported area rugs in several sizes, patterns, and colours.</li>
        <li class="tag">Large variety of high quality sofa sets from Italy in various styles and colours: black, taupe, burgundy, chocolate, stone and more.</li>
      </ul>
    </div>
  </section>

  <section class="cover">
    <h2 class="cover__lead">Massive inventory clearout of new fine furniture, homedecor, electronics &amp; accesories</h2>
    <h1 class="cover__title">PUBLIC<br>AUCTION</h1>
    <div class="cover__badge">
      <svg viewBox="0 0 180 86" width="180" height="86" aria-hidden="true">
        <path d="M14 0 H166 A14 14 0 0 0 180 14 V72 A14 14 0 0 0 166 86 H14 A14 14 0 0 0 0 72 V14 A14 14 0 0 0 14 0 Z" fill="#1d1a17"/>
      </svg>
      <p>You Can't<br>Afford To Miss<br>This Event!</p>
    </div>
    <svg class="cover__band" viewBox="0 0 320 110" preserveAspectRatio="none" aria-hidden="true">
      <path d="M0 60 Q160 10 320 40 V110 H0 Z" fill="#ef3b63"/>
    </svg>
    <div class="cover__furniture" role="img" aria-label="Black silhouettes of an urn on a side table, an armchair and a dining chair"></div>
  </section>
</body>
</html>
```